The Hop Meadow new leaflet/brochure

I would like to completely freshen up our image and make our family entertainment centre stand out when in a rack of leaflets. There are loads of photos on our website www.thehopmeadow.com there are more on our facebook page facebook.com/thehopmeadow .
I can send them all in hi res if needed. Here is a video of our place http://www.filevorta.com/file/qzt739 . I would like an A4 tri fold leaflet. I have attached the front cover of a current one. On the inside I would like a page about the parties shown on our website. You can book parties on our website now.
Reason: I am going to guarantee the prize and so will extend the deadline.
Reason: More time
Target Market(s)
Families, mums, children
Industry/Entity Type
Entertainment
Look and feel
Each slider illustrates characteristics of the customer's brand and the style your logo design should communicate.

```html
<!DOCTYPE html>
<html lang="en">
<head>
<meta charset="utf-8">
<title>The Hop Meadow – Tri-fold Leaflet</title>
<link href="https://fonts.googleapis.com/css2?family=Anton&family=Oswald:wght@500;700&family=Ubuntu:ital,wght@0,400;0,500;0,700;1,400&display=swap" rel="stylesheet">
<style>
  :root{
    --stage:#1c1c1c;
    --frame:#ffffff;
    --orange:#f07a2a;
    --amber:#f7a21b;
    --purple:#7d63b8;
    --purple-deep:#8550b4;
    --navy:#1f1a4a;
    --ink:#141414;
    --brand-blue:#3b3a9c;
    --yellow:#ffe21a;
    --white:#ffffff;
  }
  *{margin:0;padding:0;box-sizing:border-box}
  html,body{width:1200px;height:1173px;overflow:hidden;background:var(--stage)}
  .stage{position:relative;width:1200px;height:1173px;background:var(--stage)}
  .brochure{position:absolute;left:46px;top:195px;width:1097px;height:854px;background:var(--frame);border-radius:6px}
  .panels{position:absolute;left:5px;top:6px;width:1087px;height:842px;overflow:hidden;display:flex}
  .panel{position:relative;height:100%;overflow:hidden}

  /* Left panel */
  .panel-ages{width:354px;background:linear-gradient(180deg,var(--orange) 0%,#ec6a34 30%,#c85aa0 62%,var(--purple-deep) 100%);font-family:"Ubuntu",sans-serif;color:var(--ink)}
  .age-photo{position:absolute;border-radius:50%;border:4px solid #ffd9a0;box-shadow:0 0 0 5px rgba(255,150,60,.55),0 0 18px 6px rgba(255,190,80,.8)}
  .photo-babies{left:42px;top:40px;width:140px;height:140px;background:radial-gradient(circle at 45% 45%,#b59a6e,#5e7a3c 60%,#3b3226)}
  .photo-toddlers{left:198px;top:238px;width:124px;height:124px;background:radial-gradient(circle at 50% 55%,#d63b35,#6a3a30 55%,#2b2420)}
  .photo-juniors{left:228px;top:430px;width:100px;height:100px;background:radial-gradient(circle,#c8cfc4,#7d8a7c 60%,#4b5550)}
  .age-heading{position:absolute;font-family:"Anton",sans-serif;font-size:28px;line-height:34px;color:var(--navy);letter-spacing:.3px}
  .tab{position:absolute;width:25px;height:70px;background:var(--amber)}
  .age-text{position:absolute;font-size:14.5px;line-height:19.6px}
  .age-text.nowrap{white-space:nowrap}
  .age-text b{font-weight:700}

  /* Middle panel */
  .panel-offer{width:375px;background:var(--purple);font-family:"Ubuntu",sans-serif;color:var(--ink)}
  .hours-box{position:absolute;left:90px;top:40px;width:200px;height:160px;background:#261a40;border-radius:4px;color:var(--white);font-size:14px;text-align:center}
  .hours-box .hours-top{position:absolute;top:13px;width:100%}
  .hours-box .hours-bottom{position:absolute;bottom:10px;width:100%}
  .hours-photo{position:absolute;left:8px;top:38px;width:184px;height:84px;background:linear-gradient(135deg,#6a7a3a,#c9b43a 45%,#3c4a70)}
  .side-cta{position:absolute;left:-44px;top:88px;width:180px;transform:rotate(-90deg);font-family:"Anton",sans-serif;font-size:30px;line-height:34px;color:var(--ink);text-align:center;text-shadow:0 0 3px #fff,0 0 3px #fff}
  .offer-title{position:absolute;left:0;top:222px;width:100%;text-align:center;font-family:"Anton",sans-serif;font-size:44px;color:var(--navy);letter-spacing:.5px}
  .offer-title span{color:var(--yellow)}
  .offer-price{position:absolute;left:56px;top:276px;font-family:"Anton",sans-serif;font-size:48px;line-height:60px;color:var(--ink)}
  .offer-terms{position:absolute;left:172px;top:284px;font-size:18px;line-height:24px}
  .price-list{position:absolute;left:0;top:336px;width:100%;text-align:center;font-size:14px;line-height:19.5px}
  .map{position:absolute;left:38px;top:458px;width:300px;height:158px;background:linear-gradient(160deg,#eef0ee,#dfe3df);border:3px solid #111;transform:rotate(-5deg);box-shadow:0 4px 10px rgba(0,0,0,.5)}
  .find-us{position:absolute;left:35px;top:438px;font-family:"Anton",sans-serif;font-size:27px;color:var(--white);transform:rotate(-10deg);transform-origin:left bottom;letter-spacing:.5px}
  .offer-base{position:absolute;left:0;top:590px;width:375px;height:252px}
  .directions{position:absolute;left:0;top:667px;width:100%;text-align:center;font-size:12.4px;line-height:17px;font-style:italic;text-transform:uppercase}
  .contact{position:absolute;left:0;top:758px;width:100%;text-align:center;font-size:14.5px;line-height:20px;font-style:italic;text-transform:uppercase}

  /* Right panel */
  .panel-cover{width:358px;background:radial-gradient(circle at 50% 62%,#ffe47a 0%,#f6b03a 18%,#ec6f3e 40%,#d65a93 75%,#b651b0 100%);font-family:"Oswald",sans-serif;color:var(--ink);text-align:center}
  .cover-wave{position:absolute;left:0;top:0;width:358px;height:90px}
  .brand{position:absolute;left:0;top:198px;width:100%;display:flex;align-items:center;justify-content:center;gap:10px}
  .brand-dot{width:18px;height:18px;border-radius:50%;background:var(--brand-blue)}
  .brand-name{font-family:"Ubuntu",sans-serif;font-weight:700;font-size:33px;color:var(--brand-blue)}
  .tagline{position:absolute;left:0;top:257px;width:100%;font-family:"Ubuntu",sans-serif;font-size:14.5px}
  .amazing{position:absolute;left:0;top:286px;width:100%;font-size:29px;font-weight:700}
  .size{position:absolute;left:0;top:326px;width:100%;font-size:46px;font-weight:700;color:var(--brand-blue)}
  .size small{font-size:28px}
  .play-centre{position:absolute;left:0;top:384px;width:100%;font-size:29px;font-weight:700}
  .play-time{position:absolute;left:0;top:448px;width:100%;font-family:"Anton",sans-serif;font-size:40px;line-height:41px;letter-spacing:5px;color:var(--ink);text-shadow:0 0 4px #fff}
  .largest{position:absolute;left:0;top:578px;width:100%;font-size:24px;line-height:31px;font-weight:700}
  .cta-band{position:absolute;left:-10px;top:697px;width:390px;height:120px;background:var(--yellow);transform:rotate(-8deg);transform-origin:left top}
  .cta-text{position:absolute;left:72px;top:688px;width:200px;font-family:"Anton",sans-serif;font-size:30px;line-height:34px;color:var(--ink);transform:rotate(-9deg);text-shadow:0 0 3px #fff,0 0 3px #fff}
  .cover-foot{position:absolute;left:0;top:784px;width:100%;height:58px;background:var(--purple-deep)}
  .cover-url{position:absolute;left:0;top:793px;width:100%;font-family:"Ubuntu",sans-serif;font-size:17px;color:var(--white)}
</style>
</head>
<body>
<div class="stage">
  <div class="brochure">
    <div class="panels">

      <section class="panel panel-ages">
        <div class="age-photo photo-babies" role="img" aria-label="Photo of a toddler holding a ball in the soft play area"></div>
        <div class="tab" style="left:326px;top:21px"></div>
        <h2 class="age-heading" style="left:212px;top:22px">FOR THE<br>BABIES</h2>
        <p class="age-text" style="left:211px;top:92px;width:140px">Soft Play Centre including shapes, puzzles, rockers and games, interactive panels and building blocks.</p>

        <div class="tab" style="left:1px;top:221px"></div>
        <h2 class="age-heading" style="left:37px;top:225px">FOR THE<br>TODDLERS</h2>
        <div class="age-photo photo-toddlers" role="img" aria-label="Photo of a child driving a small ride-on kart"></div>
        <p class="age-text nowrap" style="left:34px;top:303px">Recommended for<br>ages up to 5 years<br>Giant Interactive Ball<br>Pool with juggler,<br>&nbsp;lifter &amp; shower, Wavy Slide, Tube Slide,<br>climbing and obstacle features.</p>

        <div class="tab" style="left:1px;top:436px"></div>
        <h2 class="age-heading" style="left:35px;top:438px">FOR THE<br>JUNIORS</h2>
        <div class="age-photo photo-juniors" role="img" aria-label="Photo of children playing inside the netted play frame"></div>
        <p class="age-text nowrap" style="left:33px;top:507px">The Hop Meadow has a gigantic<br>indoor play area, separate<br>sports area and a toddler’s activity area.<br>There are also motorised ride on karts,<br>fun sized bowling, games area and cafe<br>serving lovely coffee, snacks and meals for all<br>the family. We have the seating for over<br>600 people and over 22,000 SQFT of fun<br>for all the family and we will soon have our<br>amazing ice rink too.<br>At The Hop Meadow we certainly put the<br>emphasis on FUN! Our huge indoor<br>playground is spread over 5 levels that boasts<br>exciting features such as the :-<br><b>• Ball cannon battle zone • Skyglide track<br>• 4 Lane Astra slide • Giant ball pools</b></p>
      </section>

      <section class="panel panel-offer">
        <div class="side-cta">Book A Party!<br>Online Now</div>
        <div class="hours-box">
          <div class="hours-top">Open 7 days</div>
          <div class="hours-photo" role="img" aria-label="Photo of the multi-level indoor play frame"></div>
          <div class="hours-bottom">a week 9.00am - 6.30pm</div>
        </div>
        <h2 class="offer-title">SPECIAL <span>OFFER</span></h2>
        <div class="offer-price">£1.99</div>
        <p class="offer-terms">Any school day<br>Any time, Any age</p>
        <p class="price-list">Under 1’s £1.00 ( Free with a paying sibling)<br>Under 4’s £3.75<br>4 and overs £4.95<br>Adults £2.00 (One off registration fee)</p>
        <div class="map" role="img" aria-label="Street map showing the location of the play centre"></div>
        <h3 class="find-us">HOW TO FIND US</h3>
        <svg class="offer-base" viewBox="0 0 375 252" aria-hidden="true">
          <path d="M0 48 C80 8 170 20 250 32 C310 40 350 30 375 22 L375 252 L0 252 Z" fill="#f7a21b"/>
          <path d="M0 40 C80 0 170 12 250 24 C310 32 350 22 375 14" fill="none" stroke="#f7a21b" stroke-width="4"/>
        </svg>
        <p class="directions">From the motorway exit J12 off the M9<br>follow signs to Brynford<br>go straight over first 2 roundabouts<br>take the second exit off the 3rd<br>roundabout then take the first left</p>
        <p class="contact">Tel: 01632 960418<br>Web: www.thehopmeadow.com<br>Email: info@thehopmeadow.com</p>
      </section>

      <section class="panel panel-cover">
        <svg class="cover-wave" viewBox="0 0 358 90" aria-hidden="true">
          <path d="M0 0 L358 0 L358 20 C280 40 150 30 60 55 C30 63 10 72 0 78 Z" fill="#ffe21a"/>
          <path d="M0 92 C60 60 170 50 358 30" fill="none" stroke="#ffe21a" stroke-width="3"/>
        </svg>
        <div class="brand"><span class="brand-dot"></span><span class="brand-name">The Hop Meadow</span></div>
        <p class="tagline">Children’s Indoor Soft Adventure Play Centre</p>
        <p class="amazing">Amazing</p>
        <p class="size">22,000<small>sqft</small></p>
        <p class="play-centre">Play Centre</p>
        <p class="play-time">IT’S<br>PLAY<br>TIME!</p>
        <p class="largest">’WALES’ LARGEST DEDICATED<br>SOFT PLAY CENTRE</p>
        <div class="cta-band"></div>
        <p class="cta-text">Book A Party!<br>Online Now</p>
        <div class="cover-foot"></div>
        <p class="cover-url">www.thehopmeadow.com</p>
      </section>

    </div>
  </div>
</div>
</body>
</html>
```